pet resort day care for our buisiness

we need a new web design for our pet center in Florida , we are provide the following services -
1. dog day car
2.dog/cat boarding
3. dog grooming
4. Dog training
5.pet food toy and clothing
our current websit is -http://www.wellowbyanimalhaven.com/
we are looking for a fresh new design that will reflect the change that we have made in the vusness from renovationnto the facelaty new management and new servises
Target Market(s)
Dog Lover , Upmarket
Industry/Entity Type
Pet
Number of Pages Required
5+ page
Font styles to use
Sans Serif
Requirements
Must have
- clean design , easy to understand and navigate , our target is the upmarket costumer how are dog lover
Should not have
- NOOO of the shelf design , confusing design , brown colors

```html
<!DOCTYPE html>
<html lang="en">
<head>
<meta charset="utf-8">
<title>Wellowby Pet Center</title>
<link rel="stylesheet" href="https://fonts.googleapis.com/css2?family=Dosis:wght@500;600&family=PT+Sans:wght@400;700&display=swap">
<style>
  :root {
    --pink: #e9496c;
    --lime: #c7dc62;
    --lime-text: #b3d45a;
    --slate: #56667a;
    --ink: #2b2b2b;
    --white: #ffffff;
    --photo-cream: #f1e4e2;
    --photo-blue: #3fa6d6;
    --photo-magenta: #d4337f;
    --photo-gold: #e3b984;
  }
  * { box-sizing: border-box; margin: 0; padding: 0; }
  html, body { width: 1200px; height: 885px; overflow: hidden; }
  body { font-family: "PT Sans", sans-serif; color: var(--ink); background: var(--white); }
  .page { position: relative; width: 1200px; height: 885px; overflow: hidden; }

  .hero-photo {
    position: absolute; inset: 0 0 36px 0;
    background:
      radial-gradient(ellipse 260px 300px at 560px 520px, rgba(227,185,132,.85), rgba(227,185,132,0) 70%),
      radial-gradient(ellipse 300px 380px at 880px 420px, rgba(240,200,170,.8), rgba(240,200,170,0) 70%),
      radial-gradient(ellipse 520px 260px at 260px 760px, rgba(212,51,127,.85), rgba(212,51,127,0) 75%),
      radial-gradient(ellipse 340px 260px at 1120px 420px, rgba(63,166,214,.75), rgba(63,166,214,0) 75%),
      linear-gradient(180deg, #eadcdc 0%, var(--photo-cream) 45%, #d9a0b8 100%);
  }
  .hero-photo::after {
    content: ""; position: absolute; inset: 0;
    background: linear-gradient(90deg, rgba(255,255,255,.35) 0%, rgba(255,255,255,.15) 55%, rgba(255,255,255,0) 100%);
  }

  .brand { position: absolute; left: 114px; top: 40px; width: 148px; height: 148px; }
  .brand-ring { position: absolute; inset: 0; border: 6px solid var(--slate); border-radius: 50%; }
  .brand-name {
    position: absolute; left: 0; right: 0; top: 54px; text-align: center;
    font-family: "PT Sans", sans-serif; font-weight: 700; font-size: 21px; line-height: 1.1;
    color: var(--lime-text);
  }

  .phone {
    position: absolute; right: 64px; top: 36px;
    font-family: "PT Sans", sans-serif; font-weight: 700; font-size: 40px; color: var(--lime-text);
    letter-spacing: .5px;
  }
  .main-nav { position: absolute; right: 64px; top: 116px; display: flex; gap: 22px; }
  .main-nav a {
    font-family: "PT Sans", sans-serif; font-size: 17px; color: var(--ink);
    text-decoration: none; text-transform: uppercase; letter-spacing: .2px;
  }

  .intro { position: absolute; left: 98px; top: 250px; width: 560px; }
  .intro-title {
    font-family: "Dosis", sans-serif; font-weight: 500; font-size: 42px; line-height: 1;
    color: var(--pink); text-transform: uppercase; letter-spacing: .3px; white-space: nowrap;
  }
  .intro-lead { margin-top: 16px; font-size: 20px; line-height: 31px; color: #2f2f2f; }
  .intro-body { margin-top: 14px; font-size: 14.5px; line-height: 24px; color: #333; width: 540px; }

  .book-btn {
    position: absolute; left: 95px; top: 585px; width: 223px; height: 54px;
    background: var(--pink); border: 3px solid var(--white); border-radius: 8px;
    color: var(--white); font-family: "Dosis", sans-serif; font-weight: 500; font-size: 24px;
    text-transform: uppercase; display: flex; align-items: center; justify-content: center;
    text-decoration: none;
  }

  .location {
    position: absolute; left: 754px; top: 503px; width: 312px; height: 312px; border-radius: 50%;
    background: var(--lime); border: 3px solid var(--white);
    display: flex; flex-direction: column; align-items: center; justify-content: center;
    text-align: center; color: #222;
  }
  .location-kicker { font-size: 17px; }
  .location-address { margin-top: 6px; font-size: 20px; line-height: 31px; }
  .location-map { margin-top: 28px; font-size: 20px; font-weight: 700; color: #1d1d1d; text-decoration: none; }

  .site-footer {
    position: absolute; left: 0; bottom: 0; width: 100%; height: 36px; background: var(--slate);
    color: #e6e9ee; font-size: 12px; display: flex; align-items: center; justify-content: center;
  }
</style>
</head>
<body>
<div class="page">
  <div class="hero-photo" role="img" aria-label="Photo of a young girl hugging a golden retriever puppy on a bed with a pink polka-dot blanket and blue sheets"></div>

  <div class="brand">
    <div class="brand-ring"></div>
    <div class="brand-name">Wellowby<br>Pet Center</div>
  </div>

  <div class="phone">954-555-0142</div>
  <nav class="main-nav">
    <a href="#">Home</a>
    <a href="#">Boarding</a>
    <a href="#">Day Care</a>
    <a href="#">Training</a>
    <a href="#">Contact</a>
  </nav>

  <section class="intro">
    <h1 class="intro-title">Welcome to Wellowby Pet Center!</h1>
    <p class="intro-lead">A pet paradise providing the best pet care in the greater Fort Lauderdale FL area. Professional cat &amp; dog boarding, doggy daycare, pet grooming, training, holistic foods &amp; pet boutique.</p>
    <p class="intro-body">Discover how much Wellowby has to offer for your pet boarding needs by viewing a virtual tour of our 16,000 s/f ‘Home Away From Home’. See 9,000 s/f of air conditioned space and a 4,000 s/f outdoor playground with a splash pool. Why not just come by and take a tour of our Fort Lauderdale FL retail store, grooming salon and air conditioned suites? If you prefer to set a time that is best for you, call us on (954) 555.0142.&nbsp; We’re always happy to accommodate you.</p>
  </section>

  <a class="book-btn" href="#">Book Appointment</a>

  <aside class="location">
    <p class="location-kicker">Conveniently located at</p>
    <p class="location-address">418 SE 12th Street Fort<br>Lauderdale FL<br>just East of US1.</p>
    <a class="location-map" href="#">Click Here for map</a>
  </aside>

  <footer class="site-footer">© 2015&nbsp; Wellowby Pet Center</footer>
</div>
</body>
</html>
```